A4 Client Referral Program Flyer for Property Management Agency

Harbourline Lettings Group is a property management specialist based on Sydney's Northern Beaches in Australia.

We manage mid to high-end rental properties for investors and property owners.
We are currently looking to build our portfolio and are offering existing clients and contacts a referral incentive. We want to sign up more properties to manage.

We are offering the referrer a $250 referral fee and the new owner 2 months of free management to entice them to use Harbourline Lettings Group.

We want an A4 Flyer to print and add to other document packages we hand out to clients and suppliers.
If at all possible a matching digital banner would be great too! 1000px wide x 250px

Please find copy attached in Word Doc and our logo attached also.

Please see our website for any more details on our business.

We must be able to have an editable photoshop version (PSD) of the document as well as a print ready PDF version incl any bleed necessary for A4 printing.

Target Market(s)

30-60YO Male and Female

Industry/Entity Type

Real Estate

Font styles to use
Sans Serif

Requirements
Must have
• Company Logo, contact details and copy provided

```html
<!DOCTYPE html>
<html lang="en">
<head>
<meta charset="utf-8">
<title>Harbourline Lettings Group – Referral Program Flyer</title>
<link rel="stylesheet" href="https://fonts.googleapis.com/css2?family=Anton&family=Oswald:wght@300;400&family=Lato:ital,wght@0,400;0,700;0,900;1,900&display=swap">
<style>
  :root {
    --teal: #4bb8c4;
    --teal-dark: #3aa3b0;
    --charcoal: #414142;
    --ink: #0d0d0d;
    --paper: #ffffff;
    --mist: #f0f0f0;
    --canvas: #e9e9e9;
  }
  * { margin: 0; padding: 0; box-sizing: border-box; }
  html, body { width: 1200px; height: 1200px; overflow: hidden; }
  body { background: var(--canvas); position: relative; font-family: "Lato", sans-serif; }

  .flyer {
    position: absolute; left: 197px; top: 31px;
    width: 752px; height: 1062px;
    transform: scale(1.0718); transform-origin: top left;
    background: linear-gradient(180deg, var(--paper) 40%, var(--mist) 60%, var(--paper) 90%);
    overflow: hidden;
    box-shadow: 0 4px 18px rgba(0,0,0,.18);
  }
  .flyer__shapes { position: absolute; inset: 0; }

  .brand {
    position: absolute; left: 430px; top: 70px;
    font-family: "Lato", sans-serif; font-weight: 900; font-size: 19px;
    color: var(--ink); letter-spacing: .3px; line-height: 1; text-transform: uppercase;
    white-space: nowrap;
  }

  .headline { position: absolute; left: 0; top: 0; width: 362px; height: 700px; font-family: "Anton", sans-serif; font-weight: 400; line-height: 1; }
  .headline span { position: absolute; left: 0; width: 362px; text-align: center; white-space: nowrap; display: block; transform-origin: center top; }
  .headline__invite { top: 467px; color: var(--teal); font-size: 96px; transform: scaleX(1.2); }
  .headline__friends { top: 566px; color: var(--ink); font-size: 64px; transform: scaleX(.81); }
  .headline__reward { top: 640px; color: var(--teal); font-size: 38px; transform: scaleX(.96); }

  .offer { position: absolute; left: 513px; top: 0; width: 200px; height: 720px; color: var(--ink); line-height: 1; font-weight: 400; }
  .offer span { position: absolute; left: 0; display: block; white-space: nowrap; transform-origin: left top; }
  .offer__lead { top: 485px; font-family: "Oswald", sans-serif; font-weight: 400; font-size: 37px; transform: scaleX(1.16); }
  .offer__months { top: 523px; font-family: "Oswald", sans-serif; font-weight: 300; font-size: 40px; color: var(--paper); transform: scaleX(1.2); }
  .offer__free { top: 573px; font-family: "Anton", sans-serif; font-size: 96px; letter-spacing: -2px; transform: scaleX(1.16); }
  .offer__service { top: 668px; font-family: "Oswald", sans-serif; font-weight: 300; font-size: 29px; color: var(--paper); transform: scaleX(1.2); }

  .terms { position: absolute; right: 50px; top: 723px; width: 330px; text-align: right; }
  .terms__title { font-weight: 900; font-style: italic; font-size: 22px; color: var(--paper); }
  .terms__body { font-size: 13px; line-height: 17.5px; color: var(--ink); margin-top: 3px; }

  .link-pill {
    position: absolute; left: 350px; top: 845px; width: 358px; height: 35px;
    background: var(--paper); border-radius: 18px;
    font-size: 13.5px; color: var(--ink); display: flex; align-items: center; padding-left: 10px;
  }
  .call { position: absolute; right: 53px; top: 906px; font-size: 30px; color: var(--ink); white-space: nowrap; }

  .footer {
    position: absolute; left: 0; right: 0; top: 990px; height: 72px;
    display: flex; align-items: center; justify-content: center;
    color: var(--paper); font-size: 16.5px; font-weight: 700; letter-spacing: .2px;
  }
</style>
</head>
<body>
  <main class="flyer">
    <svg class="flyer__shapes" viewBox="0 0 752 1062" width="752" height="1062">
      <defs>
        <linearGradient id="photoTone" x1="0" y1="0" x2="1" y2="1">
          <stop offset="0" stop-color="#dcdcdc"/>
          <stop offset=".45" stop-color="#ecdcd2"/>
          <stop offset=".75" stop-color="#e6c9b8"/>
          <stop offset="1" stop-color="#f2f2f2"/>
        </linearGradient>
        <radialGradient id="iconTone" cx=".5" cy=".45" r=".55">
          <stop offset="0" stop-color="#d9493a"/>
          <stop offset=".55" stop-color="#eeeeee"/>
          <stop offset="1" stop-color="#ffffff"/>
        </radialGradient>
        <linearGradient id="tealPanel" x1="0" y1="0" x2="0" y2="1">
          <stop offset="0" stop-color="#4fbcc7"/>
          <stop offset="1" stop-color="#45b3bf"/>
        </linearGradient>
      </defs>

      <polygon role="img" aria-label="Photo: hands offering a small model house and a set of house keys"
               points="0,0 752,0 752,458 0,330" fill="url(#photoTone)"/>

      <polygon points="350,0 752,0 752,170 428,128" fill="var(--teal)"/>
      <polygon points="362,0 752,0 752,156 432,120" fill="var(--paper)"/>

      <polygon points="0,330 752,458 752,470 0,364" fill="var(--teal-dark)"/>
      <polygon points="0,364 752,470 752,474 500,440 495,452 0,392" fill="var(--charcoal)"/>

      <polygon points="500,448 752,474 752,980 262,980" fill="url(#tealPanel)"/>
      <polygon points="436,434 490,442 320,790 296,770" fill="var(--charcoal)"/>

      <circle cx="180" cy="851" r="152" fill="var(--paper)"/>
      <circle cx="180" cy="851" r="145" fill="var(--charcoal)"/>
      <circle cx="180" cy="851" r="127" fill="var(--paper)"/>
      <circle role="img" aria-label="Illustration: house resting on a red and white life ring"
              cx="180" cy="845" r="95" fill="url(#iconTone)"/>

      <rect x="0" y="980" width="752" height="10" fill="var(--paper)"/>
      <rect x="0" y="990" width="752" height="72" fill="var(--charcoal)"/>
    </svg>

    <div class="brand">Harbourline Lettings Group</div>

    <h1 class="headline">
      <span class="headline__invite">INVITE</span>
      <span class="headline__friends">YOUR FRIENDS</span>
      <span class="headline__reward">AND RECEIVE $250</span>
    </h1>

    <h2 class="offer">
      <span class="offer__lead">&amp; THEY GET</span>
      <span class="offer__months">2 MONTHS</span>
      <span class="offer__free">FREE</span>
      <span class="offer__service">MANAGEMENT</span>
    </h2>

    <div class="terms">
      <p class="terms__title">* $250 referral fee paid</p>
      <p class="terms__body">when the owner you refer signs their property for Management with Harbourline Lettings Group. Your referral must be submitted prior to signing on our website using the referral form on this page:</p>
    </div>

    <div class="link-pill">www.harbourlinelettings.com.au/referral-program</div>
    <p class="call">Call us at: 0400 555 218</p>

    <footer class="footer">www.harbourlinelettings.com.au | referrals@harbourlinelettings.com.au</footer>
  </main>
</body>
</html>
```